A5 Flyer for Financial Services Business

I am after a re-design of our business flyer to fit in with our new branding style and logo colour scheme. Wanting something with a bit of designer flair that I could not create myself. I have included the flyer which I created which lacks style so dazzle me.

I want to use the same content.

Text for main body of flyer is

Are you a small business owner, tradie or PAVC Service Provider struggling to stay on top of your bookkeeping and compliance obligations? If so we would love to help you get back on track and take control of your business finances so that you can make informed business decisions and focus on what you do best.

We have over 20 years industry experience and, as a small business ourselves, we are able to offer our clients a personal bookkeeping solution tailored to meet the needs of your business.

Accounts Payable | Accounts Receivable
Customer Invoicing
Bank and Credit Card Reconciliations
Payroll | Superannuation | Payroll Tax
Business Activity | Instalment Activity Statements
Regular Financial Reports
Ledgerly and BookNest Set-Up and Training

```html
<!DOCTYPE html>
<html lang="en">
<head>
<meta charset="utf-8">
<title>Even Ledger Financial Services – Bookkeeping Flyer</title>
<link href="https://fonts.googleapis.com/css2?family=Oswald:wght@400;500;600&family=Montserrat:wght@300;400;600;700&display=swap" rel="stylesheet">
<style>
  :root{
    --teal:#008a93;
    --teal-deep:#006f7a;
    --green:#5aac3c;
    --charcoal:#2b2b2d;
    --grey-stripe:#3d3f42;
    --ink:#231f20;
    --paper:#ffffff;
    --backdrop:#eeeeee;
    --soft:#f6f6f7;
  }
  *{box-sizing:border-box;margin:0;padding:0}
  html,body{width:1200px;height:1200px;overflow:hidden;background:var(--backdrop)}
  .flyer{position:absolute;left:210px;top:48px;width:780px;height:1104px;background:var(--paper);overflow:hidden;font-family:"Montserrat",sans-serif;color:var(--ink)}
  .header{position:absolute;left:0;top:0;width:780px;height:419px}
  .header svg{position:absolute;left:0;top:0}
  .brand{position:absolute;left:28px;top:70px;width:320px;display:flex;align-items:center;gap:14px}
  .brand-dot{width:44px;height:44px;border-radius:50%;background:var(--teal);flex:none}
  .brand-name{font-family:"Montserrat",sans-serif;font-weight:300;color:var(--teal-deep);font-size:27px;line-height:1.05;letter-spacing:.5px}
  .brand-name small{display:block;font-size:13.5px;letter-spacing:5.2px;margin-top:6px}
  .brand-rule{position:absolute;left:0;top:193px;width:420px;height:6px;background:linear-gradient(#e4e4e4,rgba(255,255,255,0))}
  .headline{position:absolute;left:26px;top:226px;font-family:"Oswald",sans-serif;line-height:1}
  .headline .lead{display:block;color:var(--teal);font-weight:600;font-size:68px;letter-spacing:-1px}
  .headline .sub{display:block;color:var(--charcoal);font-weight:400;font-size:50px;letter-spacing:-1px;line-height:1;margin-top:2px}
  .intro{position:absolute;left:0;top:419px;width:780px;height:181px;background:var(--teal);color:#fff;padding:14px 30px 0 30px;font-size:14.6px;line-height:21px;text-align:justify}
  .intro p+p{margin-top:20px}
  .intro strong{font-weight:700}
  .services{position:absolute;left:0;top:600px;width:780px;height:504px;background:linear-gradient(90deg,var(--soft),#fff 30%,#fff 70%,var(--soft))}
  .service{position:absolute;width:190px;margin-left:-95px;text-align:center}
  .service svg{display:block;margin:0 auto}
  .service h3{font-family:"Montserrat",sans-serif;font-weight:600;font-size:15.5px;line-height:21px;color:var(--charcoal);margin-top:8px;letter-spacing:-.3px}
  .badge{position:absolute;left:47px;top:1000px;width:60px;text-align:center}
  .badge-seal{width:56px;height:56px;border-radius:50%;border:2px solid var(--charcoal);background:#dfe86a;margin:0 auto}
  .badge p{font-size:8.5px;font-weight:700;line-height:11px;margin-top:3px}
  .phone{position:absolute;left:138px;top:1032px;display:flex;align-items:center;gap:6px;white-space:nowrap}
  .phone-number{font-family:"Oswald",sans-serif;font-weight:500;font-size:44px;line-height:1;color:var(--ink);letter-spacing:-.5px}
  .web{position:absolute;left:447px;top:1035px;width:333px;height:42px;background:var(--teal-deep);border-radius:14px 0 0 14px;color:#fff;font-family:"Oswald",sans-serif;font-size:18px;display:flex;align-items:center;padding-left:14px;white-space:nowrap}
</style>
</head>
<body>
<main class="flyer">
  <section class="header">
    <svg width="780" height="419" viewBox="0 0 780 419">
      <defs>
        <linearGradient id="photoTone" x1="0" y1="0" x2="1" y2="1">
          <stop offset="0" stop-color="#9fb6bd"/>
          <stop offset=".5" stop-color="#5d6f77"/>
          <stop offset="1" stop-color="#1f2227"/>
        </linearGradient>
      </defs>
      <polygon points="372,0 780,0 780,419 382,419 468,220" fill="url(#photoTone)" role="img" aria-label="Photo of two businesswomen in suits reviewing financial charts on a clipboard in front of an office building"/>
      <polygon points="336,0 352,0 452,220 363,419 348,419 437,220" fill="var(--green)"/>
      <polygon points="352,0 374,0 470,220 384,419 363,419 452,220" fill="var(--grey-stripe)"/>
    </svg>
    <div class="brand">
      <span class="brand-dot"></span>
      <div class="brand-name">EVEN LEDGER<small>Financial Services</small></div>
    </div>
    <div class="brand-rule"></div>
    <h1 class="headline">
      <span class="lead">BOOKKEEPING</span>
      <span class="sub">TAILORED TO YOUR</span>
      <span class="sub">BUSINESS NEEDS</span>
    </h1>
  </section>

  <section class="intro">
    <p>Are you a <strong>small business owner, tradie or PAVC Service Provider</strong> struggling to stay on top of your bookkeeping and compliance obligations? If so we would love to help you get back on track and take control of your business finances so that you can make informed business decisions and focus on what you do best.</p>
    <p>We have over <strong>20 years industry experience</strong> and, as a small business ourselves, we are able to offer our clients a personal bookkeeping solution tailored to meet the needs of your business.</p>
  </section>

  <section class="services">
    <div class="service" style="left:123px;top:36px">
      <svg width="112" height="112" viewBox="0 0 112 112">
        <path d="M4 58 A52 52 0 0 1 70 6" fill="none" stroke="var(--teal)" stroke-width="6"/>
        <circle cx="57" cy="57" r="52" fill="#fff" stroke="var(--charcoal)" stroke-width="2"/>
        <g fill="none" stroke="var(--teal-deep)" stroke-width="3">
          <rect x="32" y="30" width="34" height="46" rx="3"/>
          <rect x="50" y="48" width="30" height="38" rx="3" fill="#fff"/>
          <line x1="55" y1="56" x2="75" y2="56"/>
          <circle cx="41" cy="64" r="6"/>
          <path d="M37 48v-8M43 48v-12M49 48v-6"/>
        </g>
        <g fill="var(--teal-deep)"><rect x="55" y="62" width="5" height="4"/><rect x="63" y="62" width="5" height="4"/><rect x="71" y="62" width="5" height="4"/><rect x="55" y="70" width="5" height="4"/><rect x="63" y="70" width="5" height="4"/><rect x="71" y="70" width="5" height="4"/><rect x="55" y="78" width="5" height="4"/><rect x="63" y="78" width="5" height="4"/><rect x="71" y="78" width="5" height="4"/></g>
      </svg>
      <h3>Accounts Payable |<br>Accounts Receivable</h3>
    </div>
    <div class="service" style="left:288px;top:36px">
      <svg width="112" height="112" viewBox="0 0 112 112">
        <path d="M4 58 A52 52 0 0 1 70 6" fill="none" stroke="var(--teal)" stroke-width="6"/>
        <circle cx="57" cy="57" r="52" fill="#fff" stroke="var(--charcoal)" stroke-width="2"/>
        <rect x="35" y="28" width="42" height="54" rx="2" fill="none" stroke="var(--teal-deep)" stroke-width="3"/>
        <text x="56" y="41" text-anchor="middle" font-family="Montserrat, sans-serif" font-weight="700" font-size="8" fill="var(--teal-deep)">INVOICE</text>
        <path d="M41 50h30M41 57h30M41 64h22M41 71h18" stroke="var(--teal-deep)" stroke-width="2.5"/>
        <circle cx="75" cy="78" r="10" fill="var(--teal-deep)"/>
        <path d="M70 78l4 4 7-8" fill="none" stroke="#fff" stroke-width="2.5"/>
      </svg>
      <h3>Customer<br>Invoicing</h3>
    </div>
    <div class="service" style="left:455px;top:36px">
      <svg width="112" height="112" viewBox="0 0 112 112">
        <path d="M4 58 A52 52 0 0 1 70 6" fill="none" stroke="var(--teal)" stroke-width="6"/>
        <circle cx="57" cy="57" r="52" fill="#fff" stroke="var(--charcoal)" stroke-width="2"/>
        <rect x="26" y="34" width="54" height="32" rx="4" fill="#fff" stroke="var(--teal-deep)" stroke-width="3" transform="rotate(6 53 50)"/>
        <rect x="32" y="48" width="56" height="34" rx="4" fill="#fff" stroke="var(--teal-deep)" stroke-width="3"/>
        <rect x="32" y="54" width="56" height="7" fill="var(--teal-deep)"/>
        <rect x="37" y="68" width="14" height="8" rx="4" fill="var(--teal-deep)"/>
      </svg>
      <h3>Bank and Credit<br>Card Reconciliations</h3>
    </div>
    <div class="service" style="left:638px;top:36px">
      <svg width="112" height="112" viewBox="0 0 112 112">
        <path d="M4 58 A52 52 0 0 1 70 6" fill="none" stroke="var(--teal)" stroke-width="6"/>
        <circle cx="57" cy="57" r="52" fill="#fff" stroke="var(--charcoal)" stroke-width="2"/>
        <g fill="none" stroke="var(--teal-deep)" stroke-width="3">
          <rect x="44" y="26" width="26" height="36"/>
          <path d="M28 52v28h58V52M28 52l29 22 29-22M28 80l22-16M86 80l-22-16"/>
        </g>
        <text x="57" y="52" text-anchor="middle" font-family="Montserrat, sans-serif" font-weight="700" font-size="20" fill="var(--teal-deep)">$</text>
      </svg>
      <h3>Payroll | Superannuation<br>| Payroll Tax</h3>
    </div>

    <div class="service" style="left:198px;top:232px">
      <svg width="112" height="112" viewBox="0 0 112 112">
        <path d="M4 58 A52 52 0 0 1 70 6" fill="none" stroke="var(--teal)" stroke-width="6"/>
        <circle cx="57" cy="57" r="52" fill="#fff" stroke="var(--charcoal)" stroke-width="2"/>
        <rect x="27" y="38" width="58" height="28" rx="3" fill="var(--teal-deep)"/>
        <circle cx="56" cy="52" r="10" fill="#fff"/>
        <text x="56" y="57" text-anchor="middle" font-family="Montserrat, sans-serif" font-weight="700" font-size="13" fill="var(--teal-deep)">$</text>
        <path d="M44 86l4-14 8-6 10 6-4 14" fill="#fff" stroke="var(--teal-deep)" stroke-width="3"/>
      </svg>
      <h3>Business Activity |<br>Instalment Activity<br>Statements</h3>
    </div>
    <div class="service" style="left:393px;top:232px">
      <svg width="112" height="112" viewBox="0 0 112 112">
        <path d="M4 58 A52 52 0 0 1 70 6" fill="none" stroke="var(--teal)" stroke-width="6"/>
        <circle cx="57" cy="57" r="52" fill="#fff" stroke="var(--charcoal)" stroke-width="2"/>
        <circle cx="57" cy="42" r="15" fill="none" stroke="var(--teal-deep)" stroke-width="3.5"/>
        <text x="57" y="49" text-anchor="middle" font-family="Montserrat, sans-serif" font-weight="700" font-size="19" fill="var(--teal-deep)">$</text>
        <path d="M24 70h12l10 4h18c4 0 4 5 0 5H50M46 80h20l18-10c4-2 6 2 3 5L68 88H24z" fill="var(--teal-deep)"/>
      </svg>
      <h3>Regular Financial<br>Reports</h3>
    </div>
    <div class="service" style="left:593px;top:232px">
      <svg width="112" height="112" viewBox="0 0 112 112">
        <path d="M4 58 A52 52 0 0 1 70 6" fill="none" stroke="var(--teal)" stroke-width="6"/>
        <circle cx="57" cy="57" r="52" fill="#fff" stroke="var(--charcoal)" stroke-width="2"/>
        <text x="57" y="50" text-anchor="middle" font-family="Montserrat, sans-serif" font-weight="600" font-size="13" fill="var(--teal-deep)">Ledgerly</text>
        <text x="57" y="74" text-anchor="middle" font-family="Montserrat, sans-serif" font-weight="600" font-size="13" fill="var(--teal-deep)">BookNest</text>
      </svg>
      <h3>Ledgerly and BookNest<br>Set-Up and Training</h3>
    </div>
  </section>

  <div class="badge">
    <div class="badge-seal"></div>
    <p>BAS AGENT<br>10000000</p>
  </div>

  <div class="phone">
    <svg width="30" height="40" viewBox="0 0 34 44" aria-hidden="true">
      <path d="M8 4c3-2 6 0 7 3l2 7c1 3-1 5-3 6l-2 1c1 6 4 11 9 14l2-1c2-2 5-2 7 0l3 5c1 2 0 5-3 6-10 3-27-17-25-33 0-3 1-6 3-8z" fill="var(--teal)"/>
    </svg>
    <span class="phone-number">0400 123 456</span>
  </div>

  <div class="web">www.evenledgerfinancial.com.au</div>
</main>
</body>
</html>
```